Business Card Design Project

I need a business card design for our new logo, please check the logo at the following link:
https://www.filecrate.net/s/q7rtx2pw9kd41m/FernLoop.png
The address on the business card:
Av. Gervásio Tavares 418 sala 207
Barra da Tijuca, Rio de Janeiro, RJ
CEP: 22714-380
Brasil
Phone: +55 21 86347215
e-mail: osvaldo@fernloop.com.br
Updates
Thank you all for sending your designs, we will not provide feedback because there are too many designs, on December 3 we will pick the best design according to our point of view. Please keep posting.
Osvaldo
Industry/Entity Type
Business
Look and feel
Each slider illustrates characteristics of the customer's brand and the style your logo design should communicate.

```html
<!DOCTYPE html>
<html lang="pt-BR">
<head>
<meta charset="utf-8">
<title>FernLoop – Business Card</title>
<link rel="stylesheet" href="https://fonts.googleapis.com/css2?family=Maven+Pro:wght@400;500;700&display=swap">
<style>
  :root {
    --stage: #6e6e6e;
    --paper: #ffffff;
    --ink: #1c1c1c;
    --yellow: #fff200;
    --lime: #eefc00;
    --orange: #ffab00;
    --label: #f7a600;
    --brand-dot: #f5c400;
  }
  * { margin: 0; padding: 0; box-sizing: border-box; }
  html, body { width: 1200px; height: 1000px; overflow: hidden; }
  body {
    position: relative;
    background: var(--stage);
    font-family: "Maven Pro", Arial, sans-serif;
    color: var(--ink);
  }
  .card {
    position: absolute;
    width: 700px;
    height: 400px;
    background: var(--paper);
    overflow: hidden;
  }
  .card--front { left: 68px; top: 54px; }
  .card--back { left: 429px; top: 522px; }

  .side-bar {
    position: absolute;
    left: 0; top: 34px;
    width: 35px; height: 329px;
    background: var(--yellow);
  }
  .brand {
    position: absolute;
    display: flex;
    align-items: center;
    gap: 12px;
    font-weight: 700;
    color: var(--ink);
    letter-spacing: -0.5px;
  }
  .brand__dot {
    border-radius: 50%;
    background: var(--brand-dot);
    flex: none;
  }
  .card--front .brand { left: 70px; top: 150px; font-size: 46px; }
  .card--front .brand__dot { width: 22px; height: 22px; }

  .name-band {
    position: absolute;
    left: 371px; top: 185px;
    width: 329px; height: 59px;
    background: var(--yellow);
    text-align: right;
    padding: 14px 44px 0 0;
  }
  .name-band__name {
    font-size: 19px;
    font-weight: 400;
    letter-spacing: 0.6px;
    line-height: 22px;
    white-space: nowrap;
  }
  .name-band__role {
    font-size: 13px;
    letter-spacing: 0.5px;
    line-height: 15px;
    padding-right: 8px;
  }
  .contact {
    position: absolute;
    right: 51px; top: 254px;
    text-align: right;
    font-size: 13.5px;
    line-height: 17px;
    letter-spacing: 0.4px;
    font-style: normal;
  }
  .contact__lines { margin-bottom: 20px; }
  .contact__label { color: var(--label); }

  .waves { position: absolute; inset: 0; }
  .card--back .brand { left: 232px; top: 235px; font-size: 64px; }
  .card--back .brand__dot { width: 28px; height: 28px; }
</style>
</head>
<body>
  <section class="card card--front" aria-label="Card front">
    <div class="side-bar"></div>
    <div class="brand"><span class="brand__dot"></span><span class="brand__name">FernLoop</span></div>
    <div class="name-band">
      <p class="name-band__name">MARCELO VIANNA ROCHA</p>
      <p class="name-band__role">Executive Manager</p>
    </div>
    <address class="contact">
      <p class="contact__lines">Av. Gervásio Tavares 418 sala 207<br>Barra da Tijuca, Rio de Janeiro, RJ<br>CEP: 22714-380,Brasil</p>
      <p><span class="contact__label">phone.</span> +55 21 86347215</p>
      <p><span class="contact__label">email.</span> osvaldo@fernloop.com.br</p>
    </address>
  </section>

  <section class="card card--back" aria-label="Card back">
    <svg class="waves" viewBox="0 0 700 400" width="700" height="400" aria-hidden="true">
      <path d="M0,103 C170,235 420,365 700,318 L700,400 L0,400 Z" fill="var(--lime)"/>
      <path d="M0,175 C190,300 450,370 700,320 L700,400 L0,400 Z" fill="var(--orange)"/>
    </svg>
    <div class="brand"><span class="brand__dot"></span><span class="brand__name">FernLoop</span></div>
  </section>
</body>
</html>
```